We are an integrated facilities management company.

We aggregate everything related to facilities maintenance. Repair-replacement of equipment and facility space materials from:
Asset gathering and tracking.
Vendor screening, contracting and management.
Service requirement development.
Work order processing and management.
Invoice reconciliation.
Vendor payment.
Reporting.
Capital equipment bids and project management.

Target Market(s)

Retail, hospitality, multi-family housing, long term healthcare.

Industry/Entity Type

Maintenance

Contact Information for Business Card

Professional and bold look. (see logo zip file)

Colors
3377b5
85abd2
cedeed

Requirements
Must have
• N/A
Nice to have
• N/A
Should not have
• N/A

```html
<!DOCTYPE html>
<html lang="en">
<head>
<meta charset="utf-8">
<title>Meridian Facility Partners – Business Card</title>
<link href="https://fonts.googleapis.com/css2?family=Montserrat:wght@500;600;700&family=Roboto:wght@500&display=swap" rel="stylesheet">
<style>
  :root {
    --bg: #1c1c1c;
    --slate: #6a6c6d;
    --slate-dark: #5d5f60;
    --rule: #c9cbcc;
    --blue: #1356a6;
    --blue-light: #3377b5;
    --grey-band: #6b6d6e;
    --white: #ffffff;
    --ink: #ffffff;
  }
  * { box-sizing: border-box; margin: 0; padding: 0; }
  html, body { width: 1200px; height: 900px; overflow: hidden; }
  body {
    background: var(--bg);
    font-family: "Montserrat", Arial, sans-serif;
    position: relative;
  }
  .card {
    position: absolute;
    left: 250px;
    width: 700px;
    height: 400px;
    overflow: hidden;
    box-shadow: 0 10px 30px rgba(0,0,0,.5);
  }
  .card--back { top: 35px; background: var(--slate); }
  .card--front { top: 465px; background: var(--white); }

  .brand {
    position: absolute;
    display: flex;
    align-items: center;
    gap: 14px;
  }
  .brand__mark { width: 46px; height: 46px; }
  .brand__name {
    font-family: "Montserrat", Arial, sans-serif;
    font-weight: 700;
    font-size: 30px;
    line-height: 1;
    letter-spacing: .5px;
    text-transform: uppercase;
  }
  .card--back .brand { top: 62px; left: 0; right: 0; justify-content: center; }
  .card--back .brand__mark { background: var(--blue-light); }
  .card--back .brand__name { color: #4f86bf; }

  .card--back .divider {
    position: absolute;
    top: 182px; left: 0; right: 0;
    height: 1px; background: var(--rule);
  }
  .services {
    position: absolute;
    top: 205px; left: 40px; right: 40px;
    font-family: "Roboto", Arial, sans-serif;
    font-weight: 500;
    color: var(--ink);
    font-size: 17px;
    line-height: 27px;
    letter-spacing: .6px;
    text-align: center;
  }
  .services .sep { color: var(--blue-light); padding: 0 6px; }

  .card--front .brand { top: 92px; left: 0; right: 0; justify-content: center; }
  .card--front .brand__mark { background: var(--blue); }
  .card--front .brand__name { color: var(--blue); }

  .swoosh { position: absolute; left: 0; top: 0; width: 700px; height: 400px; }

  .contact {
    position: absolute;
    left: 40px; top: 252px;
    color: var(--white);
  }
  .contact__name { font-size: 22px; font-weight: 700; letter-spacing: 1px; text-transform: uppercase; }
  .contact__role { font-size: 16px; font-weight: 600; margin-bottom: 8px; letter-spacing: .5px; }
  .contact__line {
    display: flex; align-items: center; gap: 10px;
    font-size: 17px; font-weight: 600; line-height: 25px; letter-spacing: .4px;
  }
  .contact__line svg { width: 16px; height: 16px; flex: none; }

  .address {
    position: absolute;
    right: 36px; bottom: 24px;
    color: var(--white);
    text-align: right;
    font-size: 19px; font-weight: 600; line-height: 24px; letter-spacing: .6px;
  }
</style>
</head>
<body>

<section class="card card--back" aria-label="Card back">
  <div class="brand">
    <span class="brand__mark"></span>
    <span class="brand__name">Meridian Facility Partners</span>
  </div>
  <div class="divider"></div>
  <p class="services">
    Asset gathering and tracking<span class="sep">|</span>Vendor screening, contracting and management<br>
    Service requirement development<span class="sep">|</span>Work order processing and management<br>
    Invoice reconciliation<span class="sep">|</span>Vendor payment<span class="sep">|</span>Reporting<br>
    Capital equipment bids and project management
  </p>
</section>

<section class="card card--front" aria-label="Card front">
  <div class="brand">
    <span class="brand__mark"></span>
    <span class="brand__name">Meridian Facility Partners</span>
  </div>

  <svg class="swoosh" viewBox="0 0 700 400" aria-hidden="true">
    <path d="M0,222 C200,190 470,205 700,350 L700,400 L0,400 Z" fill="var(--grey-band)"/>
    <path d="M0,246 C220,214 480,238 700,360 L700,400 L0,400 Z" fill="var(--blue)"/>
    <path d="M0,213 C200,181 470,196 700,341" fill="none" stroke="var(--blue)" stroke-width="4"/>
  </svg>

  <div class="contact">
    <div class="contact__name">Daniel Hartley</div>
    <div class="contact__role">Managing Director</div>
    <div class="contact__line">
      <svg viewBox="0 0 16 16"><path d="M4 1.5 L6.2 4.6 L4.9 6.2 C5.8 8 7.9 10.2 9.8 11.1 L11.4 9.8 L14.5 12 L13.2 14.3 C8 14.5 1.5 8 1.7 2.8 Z" fill="none" stroke="#fff" stroke-width="1.4" stroke-linejoin="round"/></svg>
      604-555-0142
    </div>
    <div class="contact__line">
      <svg viewBox="0 0 16 16"><rect x="1.5" y="3.5" width="13" height="9" fill="none" stroke="#fff" stroke-width="1.4"/><path d="M1.5 3.5 L8 9 L14.5 3.5" fill="none" stroke="#fff" stroke-width="1.4"/></svg>
      info@meridianfacility.com
    </div>
    <div class="contact__line">
      <svg viewBox="0 0 16 16"><circle cx="8" cy="8" r="6.5" fill="none" stroke="#fff" stroke-width="1.4"/><ellipse cx="8" cy="8" rx="2.8" ry="6.5" fill="none" stroke="#fff" stroke-width="1.2"/><path d="M1.5 8 H14.5 M2.6 4.6 H13.4 M2.6 11.4 H13.4" stroke="#fff" stroke-width="1.1"/></svg>
      www.meridianfacility.com
    </div>
  </div>

  <div class="address">PO Box 318<br>Tullara Qld 4870</div>
</section>

</body>
</html>
```